Brook Medical Needs a PowerPoint Design

Brook Medical needs a PowerPoint template developed for use during presentations by our marketing department. Brook offers Medical specialty services to family physicians throughout Calgary. At Brook we pride ourselves on our commitment to our patients as well as having very short wait times and convenient locations spread throughout the communities. We offer services in Pulmonary Diagnostics as well as sleep apnea assessment and treatment. Consults from medical specialties such as Respirology, Physiatry, Internal Medicine, Occupational Medicine, Pediatric Infectious Disease, and alergy are also available.

***Please note we are not looking for you to build a presentation we just want the design of the slides for us to add content as needed****

We require an updated powerpoint template that we can use in a range of situations such as during marketing presentations or professional educational events. We would like a design that is modern and unique. We would like the mountain theme built into the design elements of the slide deck

We require a whole slide deck (Title slide; etc) for the Brook Medical Group as well as a body slide for our sleep division.

Our usual font is ArnoPro Semi Bold

Our Websites: brookairway.example brookrestclinic.example

Closest pantone color for Brook’s purple is PMS 814 2X

Target Market(s)

Physicians, medical professionals

Industry/Entity Type

Medical

Font styles to use
Other font styles liked:
• ArnoPro Semi Bold

Requirements
Must have
• Similar look and feel to sleep and medical slide
Nice to have
• Mountain design built into deck.
Should not have
• large actual images of mountains.

```html
<!DOCTYPE html>
<html lang="en">
<head>
<meta charset="utf-8">
<title>Brook Medical – Slide Template</title>
<link rel="stylesheet" href="https://fonts.googleapis.com/css2?family=Crimson+Pro:wght@600;700&family=Open+Sans:wght@400;600&display=swap">
<style>
  :root {
    --purple: #6a3e98;
    --purple-dark: #5a2f86;
    --footer-grey: #8a8a8c;
    --ink: #1c1c1c;
    --page: #e6e6e6;
    --slide: #ffffff;
    --line: #b9b4c2;
    --map: #e9e7e2;
  }
  * { box-sizing: border-box; margin: 0; padding: 0; }
  html, body { width: 849px; height: 1200px; overflow: hidden; }
  body {
    background: var(--page);
    font-family: "Open Sans", Arial, sans-serif;
    color: var(--ink);
    position: relative;
  }
  .slide {
    position: absolute;
    left: 42px;
    width: 765px;
    height: 540px;
    background: var(--slide);
    box-shadow: 0 1px 4px rgba(0,0,0,.25);
    overflow: hidden;
  }
  .slide--process { top: 40px; }
  .slide--contact { top: 620px; }

  .slide__title {
    position: absolute;
    left: 50px;
    top: 28px;
    font-family: "Crimson Pro", Georgia, serif;
    font-weight: 700;
    font-size: 34px;
    letter-spacing: .5px;
    line-height: 1;
  }
  .slide__slogan {
    position: absolute;
    left: 50px;
    top: 64px;
    font-family: "Crimson Pro", Georgia, serif;
    font-weight: 600;
    font-size: 11px;
    letter-spacing: .6px;
    color: var(--purple);
  }
  .brand {
    position: absolute;
    right: 28px;
    top: 22px;
    width: 110px;
    text-align: center;
  }
  .brand__ring {
    width: 46px; height: 46px;
    border: 2px solid var(--purple);
    border-radius: 50%;
    margin: 0 auto 4px;
  }
  .brand__name {
    font-family: "Crimson Pro", Georgia, serif;
    font-weight: 600;
    font-size: 13px;
    color: var(--purple);
    line-height: 1.1;
  }

  .slide__footer {
    position: absolute;
    left: 0; bottom: 0;
    width: 100%;
    height: 42px;
    background: var(--footer-grey);
    display: flex;
    align-items: center;
  }
  .slide__url {
    margin-left: 50px;
    font-family: "Crimson Pro", Georgia, serif;
    font-weight: 600;
    font-size: 15px;
    color: #fff;
    flex: 1;
  }
  .slide__number {
    width: 150px;
    height: 100%;
    background: var(--purple);
    color: #fff;
    font-size: 13px;
    display: flex;
    align-items: center;
    padding-left: 50px;
  }

  /* process diagram */
  .process__links { position: absolute; left: 0; top: 0; }
  .step {
    position: absolute;
    width: 148px;
    height: 100px;
    background: #fff;
    border: 1.5px solid var(--line);
    border-radius: 12px;
    box-shadow: 0 2px 4px rgba(0,0,0,.15);
    padding: 18px 0 0 26px;
  }
  .step ul { list-style: disc; padding-left: 14px; }
  .step li { font-family: "Crimson Pro", Georgia, serif; font-size: 18px; line-height: 1.3; }
  .step__tab {
    position: absolute;
    width: 96px;
    height: 30px;
    background: var(--purple);
    color: #fff;
    font-family: "Crimson Pro", Georgia, serif;
    font-weight: 600;
    font-size: 17px;
    display: flex;
    align-items: center;
    justify-content: center;
    border-radius: 3px;
  }
  .step__tab--bottom { bottom: -16px; right: -10px; }
  .step__tab--top { top: -18px; right: -10px; }
  .step--one   { left: 100px; top: 232px; }
  .step--two   { left: 270px; top: 240px; padding-top: 22px; }
  .step--three { left: 450px; top: 232px; }
  .step--four  { left: 610px; top: 240px; width: 128px; padding-top: 22px; }

  /* contact */
  .contact__details {
    position: absolute;
    left: 50px;
    top: 150px;
    width: 250px;
    font-size: 15px;
    line-height: 1.35;
  }
  .contact__details p + p { margin-top: 22px; }
  .contact__map {
    position: absolute;
    left: 330px;
    top: 140px;
    width: 410px;
    height: 290px;
    background: linear-gradient(135deg, #eeece8, var(--map) 60%, #dcdad4);
    box-shadow: 0 3px 8px rgba(0,0,0,.3);
  }
</style>
</head>
<body>

<section class="slide slide--process">
  <h1 class="slide__title">HOW WE WORK</h1>
  <p class="slide__slogan">FOLLOWED BY SLOGAN</p>
  <div class="brand"><div class="brand__ring"></div><div class="brand__name">Brook Pulmonary</div></div>

  <svg class="process__links" width="765" height="540" aria-hidden="true">
    <g fill="none" stroke="var(--line)" stroke-width="1.5">
      <path d="M160 232 C 200 170, 300 170, 340 240"/>
      <path d="M340 340 C 380 400, 480 400, 520 332"/>
      <path d="M520 232 C 560 170, 650 170, 680 240"/>
    </g>
  </svg>

  <div class="step step--one">
    <ul><li>Text 1</li><li>Text 2</li></ul>
    <div class="step__tab step__tab--bottom">your text</div>
  </div>
  <div class="step step--two">
    <div class="step__tab step__tab--top">your text</div>
    <ul><li>Text 1</li><li>Text 2</li></ul>
  </div>
  <div class="step step--three">
    <ul><li>Text 1</li><li>Text 2</li></ul>
    <div class="step__tab step__tab--bottom">your text</div>
  </div>
  <div class="step step--four">
    <div class="step__tab step__tab--top">your text</div>
    <ul><li>Text 1</li><li>Text 2</li></ul>
  </div>

  <footer class="slide__footer">
    <span class="slide__url">www.brookairway.example</span>
    <span class="slide__number">06</span>
  </footer>
</section>

<section class="slide slide--contact">
  <h1 class="slide__title">CONTACT US</h1>
  <p class="slide__slogan">FOLLOWED BY SLOGAN</p>
  <div class="brand"><div class="brand__ring"></div><div class="brand__name">Brook Pulmonary</div></div>

  <div class="contact__details">
    <p>Contact us by email at info@brook.example, or by mail at YOUR COM NAME, PO Box 9495, ABCD, ABCDEFGH</p>
    <p>Visit Us: 24th Floor, ABCD LLC, Harbourline Business Tower, P.O. Box: 9495 ABCD, U.A.E.</p>
    <p>Telephone +971 4 555 0100<br>Or fax at +971 4 555 0199.</p>
  </div>

  <div class="contact__map" role="img" aria-label="Street map showing the office location"></div>

  <footer class="slide__footer">
    <span class="slide__url">www.brookairway.example</span>
    <span class="slide__number"></span>
  </footer>
</section>

</body>
</html>
```